依頼詳細
お好み焼き屋さんのTOPページのみのデザインをお願いしたいです。
コロナで減少したお客様を呼び戻すために試行錯誤しながら、このたびラーメンも提供することになりましたので、メインはお好み焼き屋さんですが、ラーメンも始めました!という画像付きで告知したいです。

集客を目的としたサイトです。
ターゲットは。お腹が空いた人になります!

レイアウト構成
・ヘッダー(ロゴのみ)
・TOP画像(画像はまだないのでフリーのもので大丈夫です)
・TOPページは画像だけでなくインパクトある感じを希望です(ザックリですみません。)
・お知らせ(3行程度)
・メニュー(テキストのみ)
・店舗情報(2店舗)テキスト
・フッター(下層ページないのでコピーライトぐらいでしょうか)
という構成です。
どこかにツマミドリと味ノートにリンクするボタンが欲しいです。
まだ素材がないため仮のフリー画像で構いません。

初心者の方でも大丈夫です!
今回は予算の都合上、低価格になってしまいましたがデザインのフィーリングが合う方は今後もご依頼する可能性があります!
サイトURL
ページ数
1ページ
希望イメージ
シンプル 複雑
単色 カラフル
暗い 明るい
日常 高級
遊び心 厳粛
未来的 伝統的
女性的 男性的
希望する色
無彩色系
納品ファイル
• 高解像度JPG (.jpg)
• イラストレーター形式 (.ai)
• フォトショップ形式 (.psd)
• PNG形式 (.png)
補足説明
納品はできれば、XDが希望です。
難しい場合はご相談ください。

お客様のイメージに一番近かったため選びました!

この度は、とても素晴らしいデザインのご提案をいただきまして誠にありがとうございました。
どれも捨てがたいデザインなのですが、一番イメージに近いものを選びました。
また、機会がございましたら、ご依頼をさせていただければと思います。
どうぞよろしくお願いいたします。

```html
<!DOCTYPE html>
<html lang="ja">
<head>
<meta charset="utf-8">
<title>こなもん亭</title>
<link href="https://fonts.googleapis.com/css2?family=Noto+Sans+JP:wght@400;500;700&family=Noto+Serif+JP:wght@500;700;900&display=swap" rel="stylesheet">
<style>
:root{
  --black:#0e0e0e;
  --red:#b3131b;
  --red-dark:#7d0c10;
  --ink:#222;
  --muted:#666;
  --line:#d9d9d9;
  --white:#fff;
}
*{margin:0;padding:0;box-sizing:border-box}
html,body{width:1200px;height:4232px;overflow:hidden;background:var(--white)}
body{position:relative;font-family:"Noto Sans JP",sans-serif;color:var(--ink)}
.abs{position:absolute}
.header{left:0;top:0;width:1200px;height:140px;background:var(--black)}
.logo{left:540px;top:12px;width:120px;height:120px;border-radius:50%;border:3px solid var(--white);display:flex;align-items:center;justify-content:center;color:var(--white);font-family:"Noto Serif JP",serif;font-weight:900;font-size:24px;line-height:1.2;text-align:center}
.hero{left:0;top:140px;width:1200px;height:620px;overflow:hidden;background:linear-gradient(120deg,#2a1a12 0%,#5a3520 30%,#d8c4a8 55%,#efe6d6 75%,#e4d4bc 100%)}
.hero-photo{position:absolute}
.hero-catch{position:absolute;writing-mode:vertical-rl;font-family:"Noto Serif JP",serif;font-weight:900;line-height:1.1}
.catch-ramen{right:40px;top:40px;font-size:64px;color:var(--black);letter-spacing:4px}
.catch-okonomi{left:40px;top:60px;font-size:72px;color:var(--white);letter-spacing:6px}
.notice{left:0;top:760px;width:1200px;height:320px;background:var(--black);color:var(--white)}
.sec-title-light{position:absolute;left:0;width:1200px;top:40px;text-align:center;font-family:"Noto Serif JP",serif;font-weight:700;font-size:30px;letter-spacing:4px}
.notice-list{position:absolute;left:360px;top:130px;width:560px;list-style:none}
.notice-item{display:flex;align-items:center;height:48px;border-bottom:1px solid #333;font-size:16px}
.tag{width:120px;height:30px;background:var(--red);color:var(--white);font-size:14px;display:flex;align-items:center;justify-content:center;margin-right:36px}
.date{width:130px;color:#ddd}
.cta{display:flex;align-items:center;width:440px;height:100px;background:var(--red);border-radius:14px;color:var(--white);font-weight:700;font-size:26px;line-height:1.3;padding-left:30px;text-decoration:none}
.cta-icon{width:66px;height:66px;border-radius:50%;background:var(--red-dark);margin-right:60px;display:flex;align-items:center;justify-content:center;flex-shrink:0}
.covid{left:200px;top:1256px;width:800px;height:164px;border:3px solid var(--red);border-radius:8px;text-align:center}
.covid h3{color:var(--red);font-size:22px;font-weight:700;margin-top:26px}
.covid p{color:var(--red);font-size:14px;line-height:1.9;margin-top:14px}
.sec-title{position:absolute;left:0;width:1200px;text-align:center;font-family:"Noto Serif JP",serif;font-weight:700;font-size:32px;letter-spacing:4px}
.rule{position:absolute;height:2px;background:var(--line)}
.rule-red{position:absolute;height:4px;background:var(--red)}
.dish{position:absolute;width:200px;height:200px;border-radius:50%;border:6px solid #111}
.dish-label{position:absolute;font-size:20px;font-weight:700;display:flex;align-items:center;gap:10px}
.items{position:absolute;left:680px;width:400px;display:grid;grid-template-columns:200px 200px;row-gap:26px}
.item-name{font-size:18px;font-weight:700;padding-bottom:6px;border-bottom:2px solid var(--red);width:150px}
.item-price{font-size:14px;color:var(--muted);margin-top:6px}
.photo{position:absolute;width:440px;height:370px}
.store-name{position:absolute;font-family:"Noto Serif JP",serif;font-weight:700;font-size:26px}
.store-info{position:absolute;font-size:15px;line-height:2;color:#333}
.map{position:absolute;width:410px;height:210px;background:linear-gradient(135deg,#ecece8,#dcdcd6)}
.footer{left:0;top:4140px;width:1200px;height:92px;background:var(--black);color:#ccc;font-size:16px;display:flex;align-items:center;justify-content:center}
</style>
</head>
<body>
<header class="abs header"><div class="abs logo">こなもん亭</div></header>

<section class="abs hero">
  <div class="hero-photo" style="left:0;top:60px;width:560px;height:560px;background:radial-gradient(circle at 45% 45%,#7a4526,#2b170c 75%)" role="img" aria-label="お好み焼きの写真"></div>
  <div class="hero-photo" style="left:320px;top:30px;width:240px;height:180px;border-radius:50%;background:radial-gradient(circle,#8a5a34,#3a2212)" role="img" aria-label="お好み焼きの写真"></div>
  <div class="hero-photo" style="left:300px;top:420px;width:280px;height:190px;border-radius:50%;background:radial-gradient(circle,#d8cbb4,#8c7a60)" role="img" aria-label="もんじゃ焼きの写真"></div>
  <div class="hero-photo" style="left:590px;top:210px;width:470px;height:390px;border:6px solid #111;background:radial-gradient(circle,#f3eee2,#c8b999)" role="img" aria-label="もやしが乗ったラーメンの写真"></div>
  <div class="hero-catch catch-ramen">ラーメン<br>始めました</div>
  <div class="hero-catch catch-okonomi">お好み焼<br>もんじゃ焼</div>
</section>

<section class="abs notice">
  <h2 class="sec-title-light">お知らせ</h2>
  <ul class="notice-list">
    <li class="notice-item"><span class="tag">速報</span><span class="date">2023.02.15</span><span>Webサイトリニューアル</span></li>
    <li class="notice-item"><span class="tag">New</span><span class="date">2023.02.13</span><span>ラーメン販売開始</span></li>
    <li class="notice-item"><span class="tag">イベント</span><span class="date">2023.02.13</span><span>東京お好み焼き祭り参加</span></li>
  </ul>
</section>

<div class="abs" style="left:140px;top:1122px"><a class="cta"><span class="cta-icon"><svg width="34" height="34" viewBox="0 0 24 24"><path d="M4 20l2-6L16 4l4 4-10 10z" fill="#fff"/></svg></span>味ノートで<br>口コミをチェック</a></div>
<div class="abs" style="left:620px;top:1122px"><a class="cta"><span class="cta-icon"><svg width="34" height="34" viewBox="0 0 24 24"><path d="M4 20l2-6L16 4l4 4-10 10z" fill="#fff"/></svg></span>ツマミドリで<br>クーポンをチェック</a></div>

<div class="abs covid">
  <h3>コロナ感染症対策について</h3>
  <p>当店では店内の換気や消毒を行い、感染予防対策を徹底しております。<br>お客様に安心なサービスを提供できるよう心掛けております。</p>
</div>

<h2 class="sec-title" style="top:1510px">お品書き</h2>
<div class="rule" style="left:0;top:1592px;width:1200px"></div>
<div class="rule-red" style="left:520px;top:1591px;width:160px"></div>

<div class="dish" style="left:260px;top:1640px;background:radial-gradient(circle,#6b3b1e,#2a170c)" role="img" aria-label="お好み焼の写真"></div>
<div class="dish-label" style="left:300px;top:1864px"><svg width="20" height="26" viewBox="0 0 20 26"><path d="M3 2v24M3 3h13l-4 5 4 5H3" fill="#111" stroke="#111" stroke-width="2"/></svg>お好み焼</div>
<div class="items" style="top:1636px">
  <div><div class="item-name">お好み焼</div><div class="item-price">￥880(税込)</div></div>
  <div><div class="item-name">豚玉</div><div class="item-price">￥880(税込)</div></div>
  <div><div class="item-name">ミックスお好み焼</div><div class="item-price">￥1,380(税込)</div></div>
  <div><div class="item-name">チーズ豚玉</div><div class="item-price">￥1,080(税込)</div></div>
  <div><div class="item-name">特上お好み焼</div><div class="item-price">￥1,680(税込)</div></div>
  <div><div class="item-name">キムチ豚玉</div><div class="item-price">￥1,080(税込)</div></div>
</div>
<div class="rule" style="left:0;top:1952px;width:1200px"></div>

<div class="dish" style="left:260px;top:2010px;background:radial-gradient(circle,#d8cfbf,#8c8170)" role="img" aria-label="もんじゃ焼の写真"></div>
<div class="dish-label" style="left:300px;top:2234px"><svg width="20" height="26" viewBox="0 0 20 26"><path d="M3 2v24M3 3h13l-4 5 4 5H3" fill="#111" stroke="#111" stroke-width="2"/></svg>もんじゃ焼</div>
<div class="items" style="top:2006px">
  <div><div class="item-name">もんじゃ</div><div class="item-price">￥880(税込)</div></div>
  <div><div class="item-name">キムチ豚</div><div class="item-price">￥1,080(税込)</div></div>
  <div><div class="item-name">ミックスもんじゃ</div><div class="item-price">￥1,380(税込)</div></div>
  <div><div class="item-name">海鮮もんじゃ</div><div class="item-price">￥1,080(税込)</div></div>
  <div><div class="item-name">特上もんじゃ</div><div class="item-price">￥1,680(税込)</div></div>
  <div><div class="item-name">もち明太</div><div class="item-price">￥1,080(税込)</div></div>
</div>
<div class="rule" style="left:0;top:2322px;width:1200px"></div>

<div class="dish" style="left:260px;top:2370px;background:radial-gradient(circle,#f2ede2,#b9ab8f)" role="img" aria-label="ラーメンの写真"></div>
<div class="dish-label" style="left:300px;top:2594px"><svg width="20" height="26" viewBox="0 0 20 26"><path d="M3 2v24M3 3h13l-4 5 4 5H3" fill="#111" stroke="#111" stroke-width="2"/></svg>ラーメン</div>
<div class="items" style="top:2376px">
  <div><div class="item-name">醤油ラーメン</div><div class="item-price">￥880(税込)</div></div>
  <div><div class="item-name">塩ラーメン</div><div class="item-price">￥880(税込)</div></div>
  <div><div class="item-name">味噌ラーメン</div><div class="item-price">￥1,380(税込)</div></div>
</div>

<h2 class="sec-title" style="top:2790px">店舗情報</h2>
<div class="rule" style="left:0;top:2872px;width:1200px"></div>
<div class="rule-red" style="left:520px;top:2871px;width:160px"></div>

<div class="photo" style="left:160px;top:2910px;background:linear-gradient(135deg,#4a3528,#9c7b5c 60%,#d9c6a8)" role="img" aria-label="大阪店の店内写真"></div>
<div class="store-name" style="left:630px;top:2916px">お好み焼き 大阪店</div>
<div class="store-info" style="left:630px;top:2976px">大阪府大阪市浪速区なにわ町1-2-3<br>Tel.000-0000-0000<br>営業時間：10:00〜23:00　定休日：火</div>
<div class="map" style="left:640px;top:3090px" role="img" aria-label="大阪店周辺の地図"></div>

<div class="rule" style="left:0;top:3352px;width:1200px"></div>

<div class="photo" style="left:160px;top:3400px;background:linear-gradient(135deg,#3f3a36,#8a7a68 55%,#cfc3b2)" role="img" aria-label="東京店の店内写真"></div>
<div class="store-name" style="left:630px;top:3406px">お好み焼き 東京店</div>
<div class="store-info" style="left:630px;top:3466px">東京都台東区みどり町4-5-6<br>Tel.000-0000-0000<br>営業時間：10:00〜23:00　定休日：火</div>
<div class="map" style="left:640px;top:3580px" role="img" aria-label="東京店周辺の地図"></div>

<div class="rule" style="left:0;top:3860px;width:1200px"></div>

<div class="abs" style="left:140px;top:3990px"><a class="cta"><span class="cta-icon"><svg width="34" height="34" viewBox="0 0 24 24"><path d="M4 20l2-6L16 4l4 4-10 10z" fill="#fff"/></svg></span>味ノートで<br>口コミをチェック</a></div>
<div class="abs" style="left:620px;top:3990px"><a class="cta"><span class="cta-icon"><svg width="34" height="34" viewBox="0 0 24 24"><path d="M4 20l2-6L16 4l4 4-10 10z" fill="#fff"/></svg></span>ツマミドリで<br>クーポンをチェック</a></div>

<footer class="abs footer">Copyright © Konamontei Co.,Ltd.</footer>
</body>
</html>
```